Poster for a online company that buys your stuff

SwapKestrel offers a website which customers can get a instant offer for stuff their looking to sell. They then Courier the items in to us and they get paid the same day it arrives
We're looking for an eye catching design which portrays our hassle free process
We'll need your help to come up with a slogan/catch phrase and our easy 1,2,3 process so customers can see the poster and instantly have a clear understanding of what we do
1. Get an instant offer on our website
2. Send your item(s) to us
3.Get paid within 24 Hours
Industry/Entity Type
It Company
Look and feel
Each slider illustrates characteristics of the customer's brand and the style your logo design should communicate.

```html
<!DOCTYPE html>
<html lang="en">
<head>
<meta charset="utf-8">
<title>SwapKestrel – Sell your products easily</title>
<link rel="stylesheet" href="https://fonts.googleapis.com/css2?family=Arimo:wght@400;700&display=swap">
<style>
  :root {
    --green-light: #86c726;
    --green-mid: #2ea043;
    --green-deep: #17913a;
    --green-dark: #0b5a33;
    --green-band: #1d7a30;
    --lime: #8dc63f;
    --lime-pale: #c9e08e;
    --ink: #2a2a2a;
    --white: #ffffff;
  }
  * { box-sizing: border-box; margin: 0; padding: 0; }
  html, body { width: 900px; height: 1200px; overflow: hidden; background: var(--green-dark); }
  .poster {
    position: relative;
    width: 900px;
    height: 1200px;
    overflow: hidden;
    font-family: "Arimo", Arial, sans-serif;
    color: var(--white);
    background: radial-gradient(ellipse 70% 55% at 50% 18%, var(--green-light) 0%, #4fb02c 55%, var(--green-deep) 100%);
  }
  .backdrop { position: absolute; inset: 0; }
  .mascot {
    position: absolute;
    left: 270px;
    top: 40px;
    width: 360px;
    height: 370px;
    border-radius: 40%;
    background: radial-gradient(ellipse at 50% 45%, #f2a23a 0%, #b9d36a 45%, rgba(134,199,38,0) 72%);
  }
  .brand {
    position: absolute;
    top: 418px;
    width: 100%;
    text-align: center;
    font-weight: 700;
    font-size: 62px;
    letter-spacing: -1.5px;
    color: var(--ink);
  }
  .headline { position: absolute; top: 640px; width: 100%; text-align: center; }
  .headline-lead { font-size: 36px; letter-spacing: 0.5px; line-height: 1; }
  .headline-key {
    margin-top: 10px;
    font-size: 112px;
    letter-spacing: 10px;
    line-height: 1;
    color: var(--lime);
  }
  .headline-tail { margin-top: 10px; font-size: 38px; font-weight: 700; line-height: 1; }
  .steps { position: absolute; inset: 0; pointer-events: none; }
  .step {
    position: absolute;
    top: 1035px;
    width: 240px;
    text-align: center;
    font-size: 20px;
    line-height: 1.15;
  }
  .step-number { position: absolute; top: 885px; font-size: 28px; }
  .call-bar { position: absolute; left: 0; top: 1118px; width: 900px; height: 82px; }
  .call-label {
    position: absolute;
    left: 55px;
    top: 1132px;
    font-size: 52px;
    line-height: 1;
  }
  .call-number {
    position: absolute;
    left: 365px;
    top: 1130px;
    font-size: 56px;
    font-weight: 700;
    line-height: 1;
    letter-spacing: 1px;
  }
</style>
</head>
<body>
<main class="poster">
  <svg class="backdrop" width="900" height="1200" viewBox="0 0 900 1200" aria-hidden="true">
    <path d="M0 640 C 200 480 560 470 900 600 L900 1200 L0 1200 Z" fill="var(--lime-pale)"/>
    <path d="M0 655 C 210 510 570 500 900 625 L900 1200 L0 1200 Z" fill="#3aa84a"/>
    <path d="M0 690 C 230 560 600 540 900 660 L900 1200 L0 1200 Z" fill="var(--green-band)"/>
    <path d="M0 720 C 250 600 620 585 900 690 L900 1200 L0 1200 Z" fill="var(--green-dark)"/>
  </svg>

  <div class="mascot" role="img" aria-label="Cartoon courier mascot in a green cap giving a thumbs up and carrying an orange parcel"></div>
  <div class="brand">SwapKestrel</div>

  <section class="headline">
    <p class="headline-lead">SELL YOUR PRODUCTS</p>
    <p class="headline-key">EASILY</p>
    <p class="headline-tail">IN 3 SIMPLE STEPS</p>
  </section>

  <svg class="steps" width="900" height="1200" viewBox="0 0 900 1200" aria-hidden="true">
    <g stroke="#3f9c55" stroke-width="1.5" fill="none">
      <line x1="463" y1="838" x2="463" y2="866"/>
      <line x1="198" y1="866" x2="719" y2="866"/>
      <line x1="198" y1="866" x2="198" y2="900"/>
      <line x1="463" y1="866" x2="463" y2="900"/>
      <line x1="719" y1="866" x2="719" y2="900"/>
    </g>
    <g fill="var(--ink)" stroke="var(--lime)" stroke-width="9">
      <circle cx="198" cy="964" r="60"/>
      <circle cx="463" cy="964" r="60"/>
      <circle cx="719" cy="964" r="60"/>
    </g>
    <!-- globe -->
    <g stroke="var(--white)" stroke-width="2.5" fill="none">
      <circle cx="198" cy="964" r="26"/>
      <ellipse cx="198" cy="964" rx="11" ry="26"/>
      <line x1="198" y1="938" x2="198" y2="990"/>
      <line x1="172" y1="964" x2="224" y2="964"/>
      <path d="M176 950 H220 M176 978 H220"/>
    </g>
    <!-- trolley -->
    <g stroke="var(--white)" stroke-width="2.5" fill="none">
      <path d="M438 940 h8 v40 h42"/>
      <rect x="452" y="948" width="30" height="26"/>
      <path d="M462 948 v26 M472 948 v26"/>
      <circle cx="452" cy="988" r="4"/>
      <circle cx="482" cy="988" r="4"/>
    </g>
    <!-- 24h payment -->
    <g stroke="var(--white)" stroke-width="3" fill="none">
      <path d="M697 952 A 27 27 0 1 1 705 985"/>
      <path d="M690 946 l7 8 l9 -5"/>
    </g>
    <g fill="var(--white)" font-family="Arimo, Arial, sans-serif" font-weight="700">
      <text x="728" y="958" font-size="17" text-anchor="middle">P</text>
      <text x="710" y="982" font-size="19" text-anchor="middle">24h</text>
    </g>
    <path d="M0 1118 H318 L358 1192 H0 Z" fill="var(--green-deep)"/>
    <rect x="0" y="1192" width="900" height="8" fill="var(--green-deep)"/>
  </svg>

  <span class="step-number" style="left:150px">1</span>
  <span class="step-number" style="left:416px">2</span>
  <span class="step-number" style="left:672px">3</span>
  <p class="step" style="left:78px">Get an instant<br>offer on our website</p>
  <p class="step" style="left:343px">Send your<br>item(s) to us</p>
  <p class="step" style="left:599px">Get paid<br>within 24 Hours</p>

  <p class="call-label">Call us:</p>
  <p class="call-number">077- 4412- 8036</p>
</main>
</body>
</html>
```